Support Information Brochure relmfalke online shop

We are an online shop for automation equipment and we ship small instruction brochures with our products. The brochures are printed in DIN A4 and folded to DIN Long (1/3 A4). Please see .odt files (open document text) enclosed. We would like to modernize and professionalize the design and would like a DIN A4 template (or DIN Long). Preferred output format would be Scribus. The design should include our logo (ai, eps files enclosed) and appear modern and lightweight. The brochures contain important information and should have a high readability.We would also like to develop our corporate color scheme and typography.
Updates

Target Market(s)

Germany, small automation companies

Font styles to use
Sans Serif

Requirements
Must have
• High readability
Nice to have
• Corporate Colour Scheme and Typography suggestions

```html
<!DOCTYPE html>
<html lang="de">
<head>
<meta charset="utf-8">
<title>relmfalke – Support-Broschüre Farbvariante</title>
<link rel="stylesheet" href="https://fonts.googleapis.com/css2?family=Lato:wght@300;400;700;900&family=Exo+2:ital,wght@1,700&display=swap">
<style>
:root{
  --orange:#f07c28;
  --orange-light:#f59a3a;
  --ink:#1b1b1b;
  --white:#ffffff;
  --stage-dark:#3b3b3d;
  --stage-light:#d9d9d9;
  --black:#111111;
  --screen-dark:#1d2430;
  --screen-light:#eceff3;
}
*{margin:0;padding:0;box-sizing:border-box}
html,body{width:1200px;height:934px;overflow:hidden}
body{position:relative;font-family:"Lato",sans-serif;background:linear-gradient(var(--stage-dark) 0 772px,var(--stage-light) 772px)}
.stage-title{position:absolute;top:42px;left:0;width:1200px;text-align:center;color:var(--white);font-weight:300;font-size:44px;letter-spacing:.5px}
.page{position:absolute;top:134px;width:525px;height:743px;overflow:hidden;background:var(--white);box-shadow:0 3px 10px rgba(0,0,0,.35)}
.page--front{left:64px}
.page--back{left:611px}
.band{position:absolute;left:0;width:100%;background:linear-gradient(90deg,var(--orange),var(--orange-light))}
.header-wave{position:absolute;left:0;top:0}
.abs{position:absolute}
.brand{position:absolute;left:34px;top:48px;display:flex;align-items:center;gap:10px;color:var(--white);font-weight:900;font-size:30px;letter-spacing:.5px}
.brand-dot{width:22px;height:22px;border-radius:50%;background:var(--white)}
.brand-url{position:absolute;left:66px;top:88px;color:var(--white);font-size:7px;font-weight:700;letter-spacing:.8px}
.product-title{font-family:"Exo 2",sans-serif;font-style:italic;font-weight:700;color:var(--orange);font-size:22px;line-height:1;white-space:nowrap}
.cover-title{font-weight:700;color:var(--ink);font-size:18px;line-height:21.6px}
.rule{position:absolute;height:1.5px}
.rule--orange{background:var(--orange)}
.rule--white{background:var(--white)}
.kicker{color:var(--orange);font-size:12px;line-height:14px;letter-spacing:.4px}
.section-title{font-weight:700;font-size:20px;line-height:1.1}
.section-title--white{color:var(--white)}
.section-title--orange{color:var(--orange)}
.section-title--light{font-weight:400;font-size:19px;line-height:22px;color:var(--white)}
.copy{font-size:10.3px;line-height:12.8px}
.copy p+p{margin-top:12.8px}
.copy--white{color:var(--white);font-weight:700}
.copy--white-light{color:var(--white);font-weight:400}
.copy--ink{color:var(--ink);font-weight:400}
.copy--ink-bold{color:var(--ink);font-weight:700}
.screen{position:absolute;border:3px solid var(--white);box-shadow:0 2px 6px rgba(0,0,0,.4)}
.screen--dark{background:linear-gradient(160deg,#2a3342,var(--screen-dark))}
.screen--light{background:linear-gradient(160deg,#f6f7f9,var(--screen-light));border-color:#e6e6e6}
</style>
</head>
<body>
<h1 class="stage-title">Lighter color</h1>

<section class="page page--front">
  <svg class="header-wave" width="525" height="250" viewBox="0 0 525 250">
    <rect width="525" height="250" fill="var(--orange)"/>
    <path d="M0 127 C150 127 300 62 525 52 L525 250 L0 250Z" fill="var(--white)"/>
    <path d="M270 98 C360 70 450 56 525 44 L525 64 C430 66 350 80 270 98Z" fill="var(--black)"/>
  </svg>
  <div class="brand"><span class="brand-dot"></span>relmfalke</div>
  <div class="brand-url">WWW.RELMFALKE.DE</div>

  <div class="abs product-title" style="left:34px;top:143px">Varnik PanelSuite</div>
  <div class="rule rule--orange" style="left:34px;top:169px;width:165px"></div>
  <div class="abs cover-title" style="left:34px;top:172px;width:190px">Remote-Zugriff über<br>VNC</div>
  <div class="rule rule--orange" style="left:34px;top:218px;width:165px"></div>
  <div class="abs kicker" style="left:34px;top:223px">KONFIGURATION CLIENT</div>
  <div class="rule rule--orange" style="left:34px;top:241px;width:165px"></div>

  <div class="screen screen--dark" style="left:254px;top:140px;width:244px;height:155px" role="img" aria-label="Bildschirmfoto der HMI-Ansicht „Digitale Funktionen“ im Remote-Viewer"></div>

  <div class="band" style="top:247px;height:251px"></div>
  <div class="screen screen--dark" style="left:254px;top:140px;width:244px;height:155px" role="img" aria-label="Bildschirmfoto der HMI-Ansicht „Digitale Funktionen“ im Remote-Viewer"></div>
  <div class="abs section-title section-title--white" style="left:34px;top:310px">WAS IST VNC?</div>
  <div class="rule rule--white" style="left:34px;top:338px;width:165px"></div>
  <div class="abs copy copy--white" style="left:34px;top:352px;width:445px">
    <p>VNC ist ein Fernsteuerungsprotokoll, mit dem Sie über Ihren PC oder ein Smartphone die Kontrolle über ein Varnik HMI im Netzwerk übernehmen können. Sie sehen dann das aktuelle Bild und Ihre Bildschirmeingaben mit Maus und Tastatur werden auf das HMI übertragen.</p>
    <p style="width:300px">VNC-Client-Programme können Sie im Internet für Fenstra, Droidos und andere Systeme herunterladen. Suchen Sie im Internet oder App-Store einfach nach „VNC-Client“.</p>
  </div>

  <div class="abs section-title section-title--orange" style="left:34px;top:540px;width:260px;font-size:19px;line-height:21.5px">Wie aktivieren Sie VNC<br>im Varnik HMI?</div>
  <div class="rule rule--orange" style="left:34px;top:589px;width:200px"></div>
  <div class="abs copy copy--ink" style="left:34px;top:601px;width:275px">
    <p>Setzen Sie Bit LB9290 im Varnik HMI auf 1, um den VNCServer zu starten. Das können Sie über einen Schalter tun oder einen Timer auf dem Common-Window, der dieses Bit beim Start des HMI aktiviert.<br>Wenn Sie Bit LB9291 aktivieren, befindet sich der VNCServer im Read-Only-Modus.</p>
  </div>
  <div class="screen screen--light" style="left:317px;top:512px;width:167px;height:194px" role="img" aria-label="Bildschirmfoto des Dialogs „Timer Component Attribute“"></div>

  <div class="band" style="top:695px;height:48px"></div>
</section>

<section class="page page--back">
  <svg class="header-wave" width="525" height="250" viewBox="0 0 525 250">
    <rect width="525" height="250" fill="var(--orange)"/>
    <path d="M0 62 C150 60 300 42 525 34 L525 250 L0 250Z" fill="var(--white)"/>
    <path d="M190 50 C300 34 420 24 525 18 L525 46 C420 46 300 48 190 50Z" fill="var(--black)"/>
  </svg>
  <div class="screen screen--light" style="left:37px;top:32px;width:164px;height:195px" role="img" aria-label="Bildschirmfoto des Dialogs „Number Input Component Attribute“"></div>
  <div class="abs copy copy--ink-bold" style="left:223px;top:74px;width:290px">
    <p>Wie kann ich den VNC-Zugriff durch ein Passwort schützen?</p>
    <p>Es gibt zwei Passwörter für die VNC-Funktion, die Sie einzeln aktivieren können:<br>In Variable LW10148 – LW10149 können Sie eine Zahl als Passwort für den VNC-Lese-Zugriff hinterlegen, z.B. über ein Number Input auf dem HMI. Dieses Passwort aktivieren Sie, indem Sie LB9293 auf 1 setzen.</p>
    <p>Um die Bedienung des HMI zu schützen, verfahren Sie genauso mit LW10146 – LW10147, das mit LB9292 aktiviert wird.</p>
  </div>

  <div class="band" style="top:247px;height:251px"></div>
  <div class="abs section-title--light" style="left:37px;top:276px;width:190px">VNC-Verbindung<br>herstellen</div>
  <div class="rule rule--white" style="left:37px;top:324px;width:190px"></div>
  <div class="abs copy copy--white-light" style="left:37px;top:330px;width:192px">
    <p>Haben Sie LB9290 auf dem HMI aktiviert und das HMI im Ethernet mit dem Client verbunden, können Sie den VNC-Client starten. Geben Sie dort die IP-Adresse des HMI ein und verbinden. Die Verbindung ist nicht verschlüsselt.</p>
    <p>Wenn Sie kein Passwort hinterlegt haben, lassen Sie das Passwort-Feld leer, falls es abgefragt wird.</p>
  </div>
  <div class="screen screen--light" style="left:245px;top:306px;width:250px;height:130px" role="img" aria-label="Bildschirmfoto des Verbindungsdialogs im Remote-Viewer mit Server-Adresse 192.168.0.100"></div>

  <div class="screen screen--dark" style="left:38px;top:518px;width:250px;height:158px" role="img" aria-label="Bildschirmfoto der HMI-Ansicht „Digitale Funktionen“ im Remote-Viewer"></div>
  <div class="abs section-title--light" style="left:323px;top:530px;color:var(--orange)">VNC-Betrieb</div>
  <div class="rule rule--orange" style="left:323px;top:557px;width:165px"></div>
  <div class="abs copy copy--ink" style="left:323px;top:563px;width:180px">
    <p>Sobald sich der VNC-Client mit dem HMI verbunden hat, sehen Sie das aktuelle HMI-Bild. Sie können es auch bedienen, wenn Sie die Bedienung nicht deaktiviert haben. Die Bedienung ist leicht verzögert. Hinweis: Alle Bildwechsel und Bedien-eingaben sind auch auf dem HMI sichtbar.</p>
  </div>

  <div class="band" style="top:695px;height:48px"></div>
</section>
</body>
</html>
```